Creation of a Velmaro Flyer design

As part of the cr% 26 # 233; ation of our soci% 26 # 233; t% 26 # 233 ;, we wish to cr% 26 # 233; er a flyer pr% 26 # 233; feeling our diff% 26 # 233; annuities% 26 # 233; s business advisory services% 26 # 233; foreign% 26 # 232; res who wish to develop their activities% 26 # 233; s in Switzerland. We want a double-sided flyer that presents% 26 # 233; society% 26 # 233; t% 26 # 233; d% 26 # 39; a c% 26 # 244; t% 26 # 233; and who presents% 26 # 233; benefits of the other. We have d% 26 # 233; j% 26 # 224; made a very basic provisional flyer to be able to present our activities. We put it to you as an example.

Target Market(s)

European companies% 26 # 233; internal% 26 # 233; res% 26 # 233; es by the market% 26 # 233; Swiss

Industry/Entity Type

Business Consultant

Colors

Designer to choose colors to be used in the design.

Requirements
Must have
• Company name and contact details
A field to detail the services
Nice to have
• Some% 26 # 233; l% 26 # 233; elements that recall Switzerland and some% 26 # 233; l% 26 # 233; elements that recall c% 26 # 244; t% 26 # 233; % 26quot; business% 26quot;

```html
<!DOCTYPE html>
<html lang="en">
<head>
<meta charset="utf-8">
<title>Velmaro Flyer</title>
<link href="https://fonts.googleapis.com/css2?family=Jost:wght@400;500;700&display=swap" rel="stylesheet">
<style>
  :root {
    --page-bg: #e4e4e4;
    --sky-top: #0890d4;
    --sky-light: #5fb2e2;
    --lake: #2cb8b5;
    --slate: #aebdcc;
    --ink: #1b2430;
    --white: #ffffff;
    --strip-url: #1f3a5a;
  }
  * { margin: 0; padding: 0; box-sizing: border-box; }
  html, body { width: 1200px; height: 959px; overflow: hidden; }
  body {
    background: var(--page-bg);
    font-family: "Jost", "Futura", sans-serif;
    position: relative;
  }
  .flyer {
    position: absolute;
    left: 280px; top: 27px;
    width: 640px; height: 905px;
    overflow: hidden;
    box-shadow: 0 6px 18px rgba(0,0,0,0.18);
  }
  .flyer-shapes { position: absolute; inset: 0; }
  .brand {
    position: absolute;
    top: 60px; right: 116px;
    display: flex; align-items: center; gap: 10px;
    color: var(--white);
    font-weight: 700; font-size: 17px; letter-spacing: 0.4px;
  }
  .brand-square {
    width: 52px; height: 52px;
    background: var(--white);
    border-radius: 12px;
  }
  .site-url {
    position: absolute;
    left: 597px; top: 52px;
    writing-mode: vertical-rl;
    transform: rotate(180deg);
    color: var(--strip-url);
    font-size: 14px; letter-spacing: 1.4px;
  }
  .headline {
    position: absolute;
    left: 77px; top: 124px;
    color: var(--white);
    font-weight: 700; font-size: 16px; line-height: 27px;
    white-space: nowrap;
  }
  .body-col {
    position: absolute;
    color: var(--ink);
    font-size: 9.4px; line-height: 13.9px;
    white-space: nowrap;
  }
  .body-col.first { left: 78px; top: 636px; }
  .body-col.second { left: 253px; top: 632px; }
  .market-note {
    position: absolute;
    left: 444px; top: 636px;
    color: var(--white);
    font-weight: 700; font-size: 9.6px; line-height: 14.2px;
    white-space: nowrap;
  }
  .footnote {
    position: absolute;
    left: 72px; top: 834px;
    color: var(--ink);
    font-size: 7.6px;
    white-space: nowrap;
  }
</style>
</head>
<body>
  <article class="flyer">
    <svg class="flyer-shapes" width="640" height="905" viewBox="0 0 640 905">
      <defs>
        <linearGradient id="skyBand" x1="0" y1="0" x2="1" y2="0.3">
          <stop offset="0" stop-color="var(--sky-top)"/>
          <stop offset="1" stop-color="var(--sky-light)"/>
        </linearGradient>
        <linearGradient id="lakeScene" x1="0" y1="0" x2="0" y2="1">
          <stop offset="0" stop-color="#3fa6e0"/>
          <stop offset="0.45" stop-color="#8a7a62"/>
          <stop offset="0.7" stop-color="#4aa8a8"/>
          <stop offset="1" stop-color="var(--lake)"/>
        </linearGradient>
        <linearGradient id="bridgeScene" x1="0" y1="0" x2="0" y2="1">
          <stop offset="0" stop-color="#6fb2dc"/>
          <stop offset="0.5" stop-color="#a4643c"/>
          <stop offset="1" stop-color="#3d6f8f"/>
        </linearGradient>
      </defs>
      <rect class="sky-band" width="640" height="905" fill="url(#skyBand)"/>
      <polygon class="lower-panel" points="0,583 570,434 570,250 640,236 640,905 0,905" fill="var(--slate)"/>
      <polygon role="img" aria-label="Photo of a lakeside castle with towers and turquoise water, mountains behind"
               points="0,300 570,300 570,434 0,583" fill="url(#lakeScene)"/>
      <path class="url-strip" d="M570 0 H640 V236 Q604 238 570 252 Z" fill="var(--white)"/>
      <rect class="frame" x="45" y="51" width="382" height="807" fill="none" stroke="var(--white)" stroke-width="1.6"/>
      <polygon role="img" aria-label="Photo of a covered wooden bridge with flower boxes and a stone water tower"
               points="253,526 569,449 571,608 252,607" fill="url(#bridgeScene)"/>
    </svg>

    <div class="brand"><span class="brand-name">Velmaro</span><span class="brand-square"></span></div>
    <div class="site-url">www.velmaro-consult.ch</div>

    <h1 class="headline">Velmaro is there to support you<br>in your administrative and<br>strategic procedures!</h1>

    <p class="body-col first">Velmaro strives to deepen the<br>understanding of your business<br>and acts as your local partner.<br>We assist you in defining<br>together all the services that best<br>meet your needs.<br>Our consulting skills are focused<br>on high added value sectors,<br>such as food and beverages,<br>fashion &amp; lifestyle, products and<br>services for leading industries<br>(pharmaceutical, chemical,<br>precision mechanics) or</p>

    <p class="body-col second">sustainable solutions (renewable<br>energies, recyclable materials).<br>From our office in Neuchatel*<br>and with our language<br>knowledges, we are able to<br>cover the whole of Switzerland.<br>Having many year of experience<br>in economic promotion and<br>business management, we are<br>familiar with the Swiss trade and<br>foreign companies wishing to<br>export to Switzerland.</p>

    <p class="market-note">The potential of the<br>Swiss market offers<br>many business<br>opportunities to foreign<br>companies, however<br>there are some tariff<br>and non-tariff barriers<br>to cope with, such as its<br>strong requirements in<br>terms of quality and<br>innovation, cultural and<br>linguistic differences,<br>specific rules applied to<br>certain products or<br>services.</p>

    <p class="footnote">*as of August 2020, we will open an office in Zurich as well</p>
  </article>
</body>
</html>
```